Eye-Catching Canva Template for Medical Conference Announcements

I need an eye-catching 4:5 (1080 x 1350 px) Canva template to announce upcoming conferences our team at KORA LUMEN TX will be attending.
The design should reflect our company branding—please use our website (https://koralumentx.example/) and attached logos for reference. It should be modern, bold, and professional, as the audience is pain management physicians.
The first version will be for the NFRQB conference (https://nfrqb.example/), happening in Orlando, FL from May 15–17, 2025. Our booth number is 317.

```html
<!DOCTYPE html>
<html lang="en">
<head>
<meta charset="utf-8">
<title>KORA LUMEN TX – NFRQB Conference</title>
<link rel="stylesheet" href="https://fonts.googleapis.com/css2?family=Poppins:wght@400;500;600;700&display=swap">
<style>
  :root {
    --navy: #021848;
    --navy-soft: #0b2a66;
    --magenta: #a8268f;
    --white: #ffffff;
    --rule: #4a5a82;
    --photo-dark: #3a3a3a;
    --photo-light: #c9c9c9;
  }
  * { margin: 0; padding: 0; box-sizing: border-box; }
  html, body {
    width: 1004px;
    height: 1200px;
    overflow: hidden;
    background: var(--navy);
  }
  .poster {
    position: relative;
    width: 1004px;
    height: 1200px;
    overflow: hidden;
    font-family: "Poppins", sans-serif;
    color: var(--white);
    background:
      radial-gradient(ellipse 420px 560px at 860px 420px, rgba(40, 70, 140, 0.35), transparent 70%),
      var(--navy);
  }
  .brand {
    position: absolute;
    left: 77px;
    top: 96px;
    display: flex;
    align-items: center;
    gap: 14px;
  }
  .brand-name {
    font-weight: 600;
    font-size: 40px;
    letter-spacing: 3px;
    color: var(--white);
    line-height: 1;
  }
  .brand-dot {
    width: 14px;
    height: 14px;
    border-radius: 50%;
    background: var(--magenta);
  }
  .event-acronym {
    position: absolute;
    left: 68px;
    top: 208px;
    font-weight: 700;
    font-size: 162px;
    line-height: 1;
    letter-spacing: -2px;
  }
  .event-word {
    position: absolute;
    left: 68px;
    top: 370px;
    font-weight: 600;
    font-size: 116px;
    line-height: 1;
    letter-spacing: -1px;
  }
  .divider {
    position: absolute;
    left: 74px;
    top: 499px;
    width: 780px;
    height: 2px;
    background: var(--rule);
  }
  .divider-accent {
    position: absolute;
    left: 129px;
    top: 496px;
    width: 113px;
    height: 8px;
    border-radius: 4px;
    background: var(--magenta);
  }
  .location {
    position: absolute;
    left: 68px;
    top: 560px;
    font-weight: 400;
    font-size: 82px;
    line-height: 1;
  }
  .dates {
    position: absolute;
    left: 68px;
    top: 675px;
    font-weight: 600;
    font-size: 68px;
    line-height: 1;
    color: var(--magenta);
    letter-spacing: -1px;
  }
  .year {
    position: absolute;
    left: 68px;
    top: 760px;
    font-weight: 400;
    font-size: 60px;
    line-height: 1;
  }
  .photo-frame {
    position: absolute;
    left: 0;
    top: 0;
  }
  .booth-band {
    position: absolute;
    left: 0;
    top: 1051px;
    width: 1004px;
    height: 149px;
    background: var(--white);
    display: flex;
    align-items: center;
    justify-content: center;
    gap: 30px;
  }
  .booth-label {
    font-weight: 400;
    font-size: 54px;
    color: var(--navy);
    letter-spacing: 1px;
  }
  .booth-number {
    font-weight: 700;
    font-size: 68px;
    color: var(--magenta);
  }
</style>
</head>
<body>
  <main class="poster">
    <div class="brand">
      <span class="brand-name">KORA LUMEN TX</span>
      <span class="brand-dot"></span>
    </div>

    <h1 class="event-acronym">NFRQB</h1>
    <div class="event-word">CONFERENCE</div>

    <div class="divider"></div>
    <div class="divider-accent"></div>

    <div class="location">Orlando, FL</div>
    <div class="dates">May 15–17</div>
    <div class="year">2025</div>

    <svg class="photo-frame" width="1004" height="1200" viewBox="0 0 1004 1200">
      <defs>
        <linearGradient id="photoTone" x1="0" y1="0" x2="1" y2="1">
          <stop offset="0" stop-color="var(--photo-light)"/>
          <stop offset="0.55" stop-color="#7a7a7a"/>
          <stop offset="1" stop-color="var(--photo-dark)"/>
        </linearGradient>
      </defs>
      <path class="frame-outer" fill="#ffffff"
        d="M474,1051 L474,760 Q474,730 500,716 L740,565 Q757,555 775,565 L1004,690 L1004,1051 Z"/>
      <path class="frame-photo" role="img"
        aria-label="Photo: clinician placing a hand on a patient's upper back, black and white with a magenta highlight"
        fill="url(#photoTone)"
        d="M494,1051 L494,772 Q494,746 516,734 L745,592 Q757,585 769,592 L1004,718 L1004,1051 Z"/>
      <path class="frame-line" fill="none" stroke="var(--magenta)" stroke-width="2"
        d="M485,1051 L485,766 Q485,739 508,726 L742,579 Q757,570 772,579 L1004,704"/>
    </svg>

    <div class="booth-band">
      <span class="booth-label">Our booth number is</span>
      <span class="booth-number">317</span>
    </div>
  </main>
</body>
</html>
```